Use monitor (event monitor)

I have developed an eventmonitor for firestations for about 2 years. now i want a redesign of this montor. i have 2 views - defaultView and alarmView. the default view shows the firestation. the cars from the firestations if they are out of order or not, a view from the actual weather, and the last firealarms of our country. The alarmview. Shows specific information about the place where a fire, or a firestation is needed. it shows on openstreetmap the positions of cars, and additional information. I want to redesign this 2 sites. ideas to look at the monitor more beautiful. for the alarmview maybe new ideas how to display the cars in the map, and maybe a better place for postioning. i want upload actual 2 images that people get a feeling for that. the monitor is mostly used with a tv or a monitor. when the people are in the firestation, they want to see the needed information. what happens, where when ..... Hope this is enough information

```html
<!DOCTYPE html>
<html lang="de">
<head>
<meta charset="utf-8">
<title>Feuerwehr Almtal – Einsatzmonitor</title>
<link href="https://fonts.googleapis.com/css2?family=Fjalla+One&family=Roboto:wght@400&family=Roboto+Condensed:wght@400;500&display=swap" rel="stylesheet">
<style>
  :root {
    --red: #c0000a;
    --red-light: #f07a7a;
    --red-mid: #e03a3a;
    --page: #e8e9ec;
    --panel-dark: #474747;
    --panel-grey: #676767;
    --row-alt: #e8e8e8;
    --text: #2a2a2a;
    --white: #ffffff;
  }
  * { box-sizing: border-box; margin: 0; padding: 0; }
  html, body { width: 1200px; height: 991px; overflow: hidden; }
  body {
    background: var(--page);
    font-family: "Roboto Condensed", "Arial Narrow", sans-serif;
    color: var(--text);
    position: relative;
  }
  .topbar {
    position: absolute; left: 0; top: 0; width: 1200px; height: 62px;
    background: var(--red); color: var(--white);
  }
  .station-name {
    position: absolute; left: 54px; top: 12px;
    font-family: "Fjalla One", sans-serif; font-size: 29px; letter-spacing: 0.3px;
  }
  .clock {
    position: absolute; right: 58px; top: 17px;
    font-family: "Roboto", sans-serif; font-size: 14px;
  }
  .gauge {
    position: absolute; top: 98px; height: 80px;
    color: var(--white); text-align: center;
    font-family: "Roboto", sans-serif; font-size: 19px; line-height: 29px;
    padding-top: 12px;
    box-shadow: 0 1px 3px rgba(0,0,0,0.25);
  }
  .gauge--primary { left: 56px; width: 538px; background: var(--panel-dark); }
  .gauge--secondary { left: 602px; width: 539px; background: var(--panel-grey); }
  .alarm-board {
    position: absolute; left: 54px; top: 206px; width: 744px; height: 667px;
    background: var(--white); border-radius: 2px;
    box-shadow: 0 1px 4px rgba(0,0,0,0.25);
  }
  .alarm-list { list-style: none; border-bottom: 1px solid #999; }
  .alarm-row { position: relative; height: 48.5px; font-size: 12.5px; font-weight: 500; }
  .alarm-row:nth-child(even) { background: var(--row-alt); }
  .alarm-row span { position: absolute; top: 17px; }
  .c-date { left: 34px; } .c-time { left: 160px; } .c-unit { left: 260px; }
  .c-type { left: 414px; top: 15px !important; } .c-place { left: 599px; }
  .region-map {
    position: absolute; left: 220px; top: 468px; width: 296px; height: 164px;
    border-radius: 30px 40px 50px 30px;
    background: linear-gradient(90deg, var(--red) 0%, var(--red-light) 35%, var(--red-mid) 60%, var(--red) 100%);
  }
  .fleet {
    position: absolute; left: 814px; top: 206px; width: 326px;
    list-style: none; box-shadow: 0 1px 4px rgba(0,0,0,0.25);
  }
  .vehicle {
    position: relative; height: 48.4px; background: var(--white);
    font-size: 12.5px; font-weight: 500;
  }
  .vehicle:nth-child(odd) { background: var(--red); color: var(--white); }
  .vehicle-name { position: absolute; left: 38px; top: 18px; }
  .vehicle-status { position: absolute; left: 204px; top: 16px; }
  .footer {
    position: absolute; left: 0; width: 1200px; top: 937px; text-align: center;
    font-family: "Roboto", sans-serif; font-size: 15px; color: #222;
  }
</style>
</head>
<body>
  <header class="topbar">
    <div class="station-name">Feuerwehr Almtal</div>
    <div class="clock">Sonntag, 29. Jan. 2017, 13:33</div>
  </header>

  <section class="gauge gauge--primary">Wasserstand Lärchbach<br>149cm</section>
  <section class="gauge gauge--secondary">Wasserstand Steinau<br>106cm</section>

  <section class="alarm-board">
    <ul class="alarm-list">
      <li class="alarm-row"><span class="c-date">29.1.2017</span><span class="c-time">13:06</span><span class="c-unit">FW Birkach</span><span class="c-type">Eigenanforderung</span><span class="c-place">6065 Birkach</span></li>
      <li class="alarm-row"><span class="c-date">29.1.2017</span><span class="c-time">12:47</span><span class="c-unit">FW Hochwang</span><span class="c-type">Technischer Einsatz</span><span class="c-place">6100 Hochwang/Tirol</span></li>
      <li class="alarm-row"><span class="c-date">29.1.2017</span><span class="c-time">11:58</span><span class="c-unit">FW Fernau</span><span class="c-type">Eigenanforderung</span><span class="c-place">6114 Fernau</span></li>
      <li class="alarm-row"><span class="c-date">29.1.2017</span><span class="c-time">11:25</span><span class="c-unit">FW Grund/Talrain</span><span class="c-type">Eigenanforderung</span><span class="c-place">6182 Grund/Talrain</span></li>
      <li class="alarm-row"><span class="c-date">29.1.2017</span><span class="c-time">10:30</span><span class="c-unit">FW Bergmahd</span><span class="c-type">Nachalarmierung</span><span class="c-place">6647 Pfannalm</span></li>
      <li class="alarm-row"><span class="c-date">29.1.2017</span><span class="c-time">10:30</span><span class="c-unit">FW Moosboden</span><span class="c-type">Unterstutzungseinsatz</span><span class="c-place">6647 Pfannalm</span></li>
      <li class="alarm-row"><span class="c-date">29.1.2017</span><span class="c-time">10:03</span><span class="c-unit">FW Rosswangle</span><span class="c-type">Eigenanforderung</span><span class="c-place">6672 Rosswangle</span></li>
      <li class="alarm-row"><span class="c-date">29.1.2017</span><span class="c-time">10:00</span><span class="c-unit">FW Auendorf-Lindach</span><span class="c-type">OL Eigenanforderung</span><span class="c-place">9990 Auendorf-Lindach</span></li>
      <li class="alarm-row"><span class="c-date">29.1.2017</span><span class="c-time">09:44</span><span class="c-unit">FW Lehnach</span><span class="c-type">Eigenanforderung</span><span class="c-place">6105 Lehnach</span></li>
    </ul>
    <div class="region-map" role="img" aria-label="Karte der Bezirke mit aktiven Einsätzen, eingefärbt nach Einsatzaufkommen"></div>
  </section>

  <ul class="fleet">
    <li class="vehicle"><span class="vehicle-name">FF Florian</span><span class="vehicle-status">Frei auf Wache</span></li>
    <li class="vehicle"><span class="vehicle-name">KDOF-1</span><span class="vehicle-status">Frei auf Wache</span></li>
    <li class="vehicle"><span class="vehicle-name">LF-1</span><span class="vehicle-status">Frei auf Wache</span></li>
    <li class="vehicle"><span class="vehicle-name">RLF-1</span><span class="vehicle-status">Frei auf Wache</span></li>
    <li class="vehicle"><span class="vehicle-name">MTF-1</span><span class="vehicle-status">Frei auf Wache</span></li>
    <li class="vehicle"><span class="vehicle-name">BOOT-1</span><span class="vehicle-status">Frei auf Wache</span></li>
    <li class="vehicle"><span class="vehicle-name">BOOT-2</span><span class="vehicle-status">Frei auf Wache</span></li>
  </ul>

  <footer class="footer">Copyright © 2018. All Rights Reserved - Privacy Policy</footer>
</body>
</html>
```